Olive Oil Label Needs Graphic Designs

We need two sister label designs for 500ml bottles for our new brand "Casa Lumbre". Casa Lumbre is a high-end olive oil from Baeza, Spain which will be sold in the US. The oil will be produced from both Arbequina olives and Picual olives. Therefore, envisioning the same design just a different color scheme for the different labels.
The label should have the following characteristics; clean and simple, stand-out from mainstream labels, be eye-catching, give perception of high-end / high-quality.
Our current thinking of what we want (but please let your creative juices flow); lighter background, to be more eye catching, graphics of and olive, a olive branch or olive tree.
Text which should appear on the label are (not necessarily in this order);
Casa Lumbre
Extra Virgin Olive Oil
Family Reserve
Arbequina (One design)
Picual (Second design)
The label should be about 3 inches wide and 5.5 inches in height.

```html
<!DOCTYPE html>
<html lang="en">
<head>
<meta charset="utf-8">
<title>Casa Lumbre — Arbequina Label</title>
<link rel="stylesheet" href="https://fonts.googleapis.com/css2?family=Barlow+Condensed:wght@300;400;600&display=swap">
<style>
  :root {
    --canvas: #f3eee3;
    --label: #141414;
    --ink: #f2f2ee;
    --ink-soft: #e4e4de;
    --olive: #8e9433;
    --olive-light: #b7bc4a;
    --olive-deep: #6f7a2a;
    --band-text: #ecebd2;
  }
  * { box-sizing: border-box; margin: 0; padding: 0; }
  html, body {
    width: 960px; height: 1200px; overflow: hidden;
    background: var(--canvas);
    font-family: "Barlow Condensed", "Arial Narrow", sans-serif;
  }
  .label {
    position: absolute; left: 200px; top: 80px;
    width: 560px; height: 1040px;
    background: var(--label);
    border-radius: 6px;
    color: var(--ink);
  }
  .category {
    position: absolute; left: 78px; top: 170px;
    font-weight: 300; font-size: 62px; line-height: 86px;
    color: var(--ink-soft); text-transform: uppercase;
  }
  .rule {
    position: absolute; left: 78px; top: 376px;
    width: 172px; height: 7px; background: var(--olive);
  }
  .brand {
    position: absolute; left: 74px; top: 404px;
    font-weight: 600; font-size: 120px; line-height: 124px;
    letter-spacing: 1px; text-transform: uppercase;
    white-space: nowrap;
  }
  .variety {
    position: absolute; left: 40px; top: 720px;
    width: 480px; height: 94px;
    background: var(--olive);
    display: flex; align-items: center;
    padding-left: 36px;
    font-weight: 400; font-size: 70px;
    color: var(--band-text); text-transform: uppercase;
  }
  .olive-art {
    position: absolute; left: 420px; top: 600px;
    width: 110px; height: 290px;
    border-radius: 55px;
    background: linear-gradient(160deg, var(--olive-deep) 0%, var(--olive-light) 55%, var(--olive) 100%);
  }
  .reserve {
    position: absolute; left: 0; right: 0; top: 900px;
    text-align: center; padding-left: 70px;
    font-weight: 300; font-size: 42px;
    color: var(--ink-soft); text-transform: uppercase;
  }
  .volume {
    position: absolute; left: 0; right: 0; top: 965px;
    text-align: center; padding-left: 10px;
    font-weight: 400; font-size: 48px;
  }
</style>
</head>
<body>
  <main class="label">
    <p class="category">Extra Virgin<br>Olive Oil</p>
    <div class="rule"></div>
    <h1 class="brand">Casa<br>Lumbre</h1>
    <div class="variety">Arbequina</div>
    <div class="olive-art" role="img" aria-label="Illustration of green olives on a sprig with slender leaves"></div>
    <p class="reserve">Family Reserve</p>
    <p class="volume">500ml</p>
  </main>
</body>
</html>
```